Verdant Medispa Business Card

need a business card for our medispa, attached please see the logo.
our website is https://verdantmedispa-example.com

Sorina Belcourt, MD
Internal Medicine

555-204-7193

Sorina@verdantmedispa-example.com

Www.Verdantmedispa-example.com

738 E Harlow Blvd N, Ste 512, Katy, TX 77981

Target Market(s)

MedSpa, Cosmetics, Esthetics

Industry/Entity Type

MedicalSpa

Contact Information for Business Card

Please see the attached business card which i pulled from the internet. I like the idea back as a logo and front with info.

Font styles to use
Decorative

Requirements
Must have
• Color should be matching with Logo and Website theme, Also I like to have QR code for the website

```html
<!DOCTYPE html>
<html lang="en">
<head>
<meta charset="utf-8">
<title>Verdant Medispa Business Card</title>
<link rel="stylesheet" href="https://fonts.googleapis.com/css2?family=Figtree:wght@400;500&display=swap">
<style>
  :root {
    --backdrop: #0d1629;
    --card: #162c55;
    --gold: #e2b593;
    --ink: #ffffff;
  }
  * { margin: 0; padding: 0; box-sizing: border-box; }
  html, body {
    width: 1200px;
    height: 1039px;
    overflow: hidden;
    background: var(--backdrop);
    font-family: "Figtree", Arial, sans-serif;
    color: var(--ink);
  }
  .canvas { position: relative; width: 1200px; height: 1039px; }
  .card {
    position: absolute;
    left: 314px;
    width: 572px;
    background: var(--card);
    border-radius: 14px;
  }
  .card--back { top: 160px; height: 327px; }
  .card--front { top: 554px; height: 328px; }

  .brand-name {
    position: absolute;
    color: var(--gold);
    font-weight: 400;
    white-space: nowrap;
  }
  .card--back .brand-name {
    left: 0; right: 0;
    top: 138px;
    text-align: center;
    font-size: 44px;
    letter-spacing: 1px;
  }
  .card--front .brand-name {
    left: 46px;
    top: 54px;
    font-size: 26px;
    letter-spacing: 0.5px;
  }

  .address, .contact-list {
    position: absolute;
    left: 304px;
    font-size: 13px;
    line-height: 16.5px;
  }
  .address { top: 47px; }
  .contact-list { top: 242px; list-style: none; }

  .person { position: absolute; left: 46px; top: 241px; }
  .person__name { font-size: 21px; font-weight: 400; line-height: 26px; }
  .person__role { font-size: 16px; line-height: 20px; }
</style>
</head>
<body>
<div class="canvas">
  <section class="card card--back">
    <p class="brand-name">Verdant MediSpa</p>
  </section>

  <section class="card card--front">
    <p class="brand-name">Verdant MediSpa</p>

    <address class="address" style="font-style:normal">
      738 E Harlow Blvd N,<br>Ste 512, Katy, TX 77981
    </address>

    <div class="person">
      <h1 class="person__name">Sorina Belcourt, MD</h1>
      <p class="person__role">Internal Medicine</p>
    </div>

    <ul class="contact-list">
      <li>P: 555-204-7193</li>
      <li>E: Sorina@verdantmedispa-example.com</li>
      <li>W: www.Verdantmedispa-example.com</li>
    </ul>
  </section>
</div>
</body>
</html>
```